High Quality fast food restaurant - Quonfel

Quonfel is a fast food company with its target's focused on logistic, simplicity, high quality, freshness and modern.

We need a web design where the customers can get a complete idea of our high quality completeness, we want to take fast food to a new upper level.

We would like to see the colours of wood and metal. Pictures have been attached of our local.

We would like to have something in similar to: http://www.zq-vorn.com/
Updates

Images for the food we are going to sell can be found here: http://trq.lk/uRTWQ

It will be the images with rice, french fries or pita bread.

Target Market(s)

The fast food eating people between sloppy food and restaurant level.

Industry/Entity Type

Fast Food Restaurant

Requirements
Should not have
• No Flash or Java

```html
<!DOCTYPE html>
<html lang="en">
<head>
<meta charset="utf-8">
<title>Quonfel – High Quality Fastfood</title>
<link rel="stylesheet" href="https://fonts.googleapis.com/css2?family=Oswald:wght@600&family=Open+Sans:ital,wght@0,400;1,400&family=Vollkorn:wght@400&family=Rye&display=swap">
<style>
:root{
  --wood-dark:#2e1a10;
  --wood-mid:#4a2c1a;
  --wood-light:#5c3821;
  --white:#ffffff;
  --ink:#1d1d1d;
  --heading:#3f4041;
  --accent:#d21f06;
  --steel-light:#f1f3f5;
  --steel-dark:#4a4e57;
  --page:#dde2e3;
  --frame:#b2b4b5;
  --field:#3a3b3d;
}
*{margin:0;padding:0;box-sizing:border-box}
html,body{width:1200px;height:1163px;overflow:hidden}
body{position:relative;background:var(--page);font-family:"Open Sans",sans-serif;color:var(--ink)}
.hero{position:absolute;left:0;top:0;width:1200px;height:654px;
  background:radial-gradient(ellipse at 50% 40%,var(--wood-light) 0%,var(--wood-mid) 45%,var(--wood-dark) 100%)}
.main-nav{position:absolute;left:188px;top:0;width:842px;height:42px;background:var(--white);
  border-radius:0 0 14px 14px;display:flex;justify-content:center;align-items:center;gap:33px}
.main-nav::after{content:"";position:absolute;left:418px;top:41px;border-left:10px solid transparent;border-right:10px solid transparent;border-top:14px solid var(--white)}
.main-nav a{font-size:14px;color:var(--ink);text-decoration:none;text-transform:uppercase}
.brand{position:absolute;left:0;top:74px;width:1200px;text-align:center;font-family:"Rye",serif;font-size:54px;color:var(--white);line-height:1}
.hero-photo{position:absolute;left:202px;top:158px;width:698px;height:496px;
  background:radial-gradient(ellipse at 45% 55%,#e7c06a 0%,#cfa15a 35%,#b9a59a 60%,rgba(90,55,35,0) 78%)}
.steel-band{position:absolute;left:0;top:654px;width:1200px;height:15px;
  background:linear-gradient(var(--steel-dark),var(--steel-light) 35%,#9aa0a8 60%,var(--steel-dark))}
.content{position:absolute;left:0;top:669px;width:1200px;height:494px;
  background:radial-gradient(ellipse at 40% 0%,#f3f5f6 0%,var(--page) 60%)}
.headline{position:absolute;left:0;top:680px;width:1200px;text-align:center;font-family:"Oswald",sans-serif;font-weight:600;font-size:54px;line-height:66px;color:var(--heading);letter-spacing:1px}
.feature{position:absolute;top:763px;width:262px}
.feature-photo{height:167px;border:9px solid var(--frame)}
.feature h2{margin-top:13px;font-family:"Vollkorn",serif;font-weight:400;font-size:14px;color:var(--accent);text-transform:uppercase;white-space:nowrap}
.feature p{margin-top:5px;padding-left:2px;font-size:12.6px;line-height:19px;width:270px}
.site-footer{position:absolute;left:190px;top:1109px;font-size:13px;line-height:19px}
.newsletter{position:absolute;left:804px;top:1091px}
.newsletter label{display:block;font-size:12px;color:var(--accent)}
.newsletter-field{margin-top:6px;width:219px;height:33px;background:var(--field);border:1px solid #222;border-radius:2px;display:flex;align-items:center;justify-content:space-between;padding:0 8px}
.newsletter-field span{font-style:italic;font-size:11.5px;color:#9a9a9a}
</style>
</head>
<body>
<header class="hero">
  <nav class="main-nav">
    <a href="#">Home</a><a href="#">Menu</a><a href="#">Fresh offers</a><a href="#">About us</a><a href="#">Free delivers</a><a href="#">Discount coupons</a>
  </nav>
  <div class="brand">Quonfel</div>
  <div class="hero-photo" role="img" aria-label="Fried fish pita with salad, fries and a bowl of yoghurt dip on a checked napkin"></div>
</header>
<div class="steel-band"></div>
<main class="content"></main>
<h1 class="headline">HIGH QUALITY FASTFOOD</h1>

<article class="feature" style="left:186px">
  <div class="feature-photo" role="img" aria-label="Grilled meat with tomato salad and peppers" style="background:linear-gradient(135deg,#7a3a20,#c8462c 45%,#d9b05a)"></div>
  <h2>Ec condimentum orci</h2>
  <p>Lorem ipsum dolor sit amet, consectetur adipiscing elit. Praesent sit amet lectus magna. Sed egestas fermentum scelerisque. Proin quam neque, pharetra ac auctor quis,</p>
</article>
<article class="feature" style="left:480px">
  <div class="feature-photo" role="img" aria-label="Kebab pita with salad and green peppers" style="background:linear-gradient(135deg,#b59470,#e6dccd 45%,#c7b24a)"></div>
  <h2>Nam eleifend vulputate ligula</h2>
  <p>Lorem ipsum dolor sit amet, consectetur adipiscing elit. Praesent sit amet lectus magna. Sed egestas fermentum scelerisque. Proin quam neque, pharetra ac auctor quis,</p>
</article>
<article class="feature" style="left:769px">
  <div class="feature-photo" role="img" aria-label="French fries in a red basket with ketchup" style="background:linear-gradient(180deg,#eeeaea,#f0c040 50%,#d8403a)"></div>
  <h2>Dolor risus auctor orci.</h2>
  <p>Lorem ipsum dolor sit amet, consectetur adipiscing elit. Praesent sit amet lectus magna. Sed egestas fermentum scelerisque. Proin quam neque, pharetra ac auctor quis,</p>
</article>

<footer class="site-footer">
  <div>Home&nbsp; //&nbsp; Menu&nbsp; //&nbsp; Fresh offers&nbsp; //&nbsp; About Us&nbsp; //&nbsp; Free Delivers&nbsp; //&nbsp; Discount Coupons</div>
  <div>Copyright by Quonfel.com</div>
</footer>
<form class="newsletter">
  <label>Newsletter Subscription</label>
  <div class="newsletter-field">
    <span>Enter email address here</span>
    <svg width="20" height="20" viewBox="0 0 20 20" aria-hidden="true"><rect x="1" y="1" width="18" height="18" fill="none" stroke="#8a8a8a" stroke-width="1.5"/><path d="M8 5l5 5-5 5" fill="none" stroke="#8a8a8a" stroke-width="1.5"/></svg>
  </div>
</form>
</body>
</html>
```